Need a website to promote and sell my book

Using images from the book, I need a website designed that helps promote the book and eventually sell it.
*Need a landing page
*About the author page
*Storefront page to purchase
*Coming soon page
*"Featured in" page that can link to news articles etc.
The images posted here are examples, the winner of the contest will get the images from the finished book. I will provide the exact text to the winner of the contest.

I can also provide images of kids reading the book. For now, I'll just use one, the winner can have them all to choose from.
Updates

Extending deadline to allow for a few more designers to submit and to allow time for me to review and hold a poll

Target Market(s)

Parents, aunts, uncles, grandparents, friends who have kids; teachers, daycare teachers, babysitters etc.

Industry/Entity Type

Custom Publishing

Coding

Coded - Design and coding required

Number of Pages Required

5+ page

Font styles to use
Sans Serif

Colors

Designer to choose colors to be used in the design.

Requirements
Must have
• It must have a fun feel like the book.
Nice to have
• Would be great to have a section that automatically pulls tweets about the book into it.

```html
<!DOCTYPE html>
<html lang="en">
<head>
<meta charset="utf-8">
<title>Margot — Author &amp; Writer</title>
<link href="https://fonts.googleapis.com/css2?family=Libre+Baskerville:ital,wght@0,400;0,700;1,400&family=Lato:wght@300;400;700&display=swap" rel="stylesheet">
<style>
:root{
  --accent:#e4583b;
  --ink:#2b2b2b;
  --body:#6f6f6f;
  --muted:#a9a9a9;
  --cream:#f3f1ea;
  --grey:#f5f5f5;
  --white:#ffffff;
}
*{box-sizing:border-box;margin:0;padding:0}
html,body{width:1200px;height:3517px;overflow:hidden;background:var(--white)}
body{font-family:'Lato',sans-serif;color:var(--body);position:relative}
section,header{position:absolute;left:0;width:1200px}
.abs{position:absolute}
.nowrap{white-space:nowrap}
.btn{position:absolute;display:flex;align-items:center;justify-content:center;gap:7px;font-family:'Lato',sans-serif;font-weight:700;font-size:11px;letter-spacing:.3px;text-transform:uppercase;background:var(--accent);color:#fff;border-radius:2px;text-decoration:none}
.btn.ghost{background:transparent;color:var(--accent);border:1.5px solid var(--accent)}
.center{left:0;width:1200px;text-align:center;white-space:nowrap}
.eyebrow{font-family:'Libre Baskerville',serif;color:var(--accent);font-size:14px;text-transform:uppercase}
.title{font-family:'Libre Baskerville',serif;color:var(--ink);font-size:41px}
.lead{font-size:11.5px;line-height:22px;color:var(--body);white-space:nowrap}

/* hero */
.hero{top:0;height:602px;background:var(--cream)}
.nav a{position:absolute;top:58px;font-family:'Libre Baskerville',serif;font-size:11.5px;color:var(--ink);text-decoration:none;text-transform:uppercase;letter-spacing:.5px}
.nav a.active{color:var(--accent);text-decoration:underline}
.brand{position:absolute;top:38px;left:466px;width:200px;text-align:center}
.brand-name{font-family:'Libre Baskerville',serif;font-size:25px;letter-spacing:3px;color:var(--ink)}
.brand-line{height:1px;background:var(--ink);width:166px;margin:3px auto 4px}
.brand-tag{font-family:'Libre Baskerville',serif;font-size:8px;letter-spacing:1.5px;color:var(--ink);text-transform:uppercase}
.hero-title{top:212px;left:138px;width:400px;text-align:center;color:var(--ink);white-space:nowrap}
.hero-title .l1{font-family:'Libre Baskerville',serif;font-weight:700;font-size:29px;letter-spacing:1.5px;text-transform:uppercase;line-height:38px}
.hero-title .l2{font-family:'Libre Baskerville',serif;font-style:italic;font-size:29px;line-height:40px;margin-top:4px}
.hero-copy{top:312px;left:160px;width:380px;font-family:'Libre Baskerville',serif;font-size:10px;line-height:22px;color:var(--muted);white-space:nowrap}
.book-visual{left:703px;top:173px;width:334px;height:325px;border-radius:4px;background:linear-gradient(100deg,#f2c56b 0%,#8cc7e4 45%,#6fb1d8 100%)}

/* welcome */
.welcome{top:602px;height:831px;background:var(--white)}
.about-label{left:166px;top:978px}
.about-head{left:161px;top:1020px;font-family:'Libre Baskerville',serif;font-weight:400;color:var(--ink);font-size:40px;line-height:45px;white-space:nowrap}
.about-copy{left:161px;top:1122px;font-size:10.5px;line-height:22.5px;white-space:nowrap}
.portrait{left:461px;top:945px;width:278px;height:415px;background:linear-gradient(180deg,#c7b7a4 0%,#7a5a48 45%,#b0162a 75%,#9c1225 100%)}
.quote-box{left:762px;top:984px;width:275px;height:336px;border:2px solid var(--accent);background:var(--cream)}
.quote-mark{font-family:'Libre Baskerville',serif;font-weight:700;color:var(--accent);font-size:34px}
.quote-text{position:absolute;left:0;top:66px;width:271px;text-align:center;font-family:'Libre Baskerville',serif;font-style:italic;color:var(--accent);font-size:19px;line-height:23px;letter-spacing:.5px;white-space:nowrap}

/* reviews */
.reviews{top:1433px;height:938px;background:var(--grey)}
.cover{position:absolute;width:202px;height:239px;background:linear-gradient(180deg,#7fc0e3 0%,#9bd0ea 55%,#f1c46b 100%)}
.review{position:absolute;width:215px;height:250px;white-space:nowrap}
.review h3{position:absolute;top:0;left:0;font-family:'Libre Baskerville',serif;font-weight:400;font-size:14.5px;line-height:30px;color:var(--ink)}
.review .by{position:absolute;top:70px;left:0;font-size:10.5px;font-style:italic;color:var(--muted)}
.review p{position:absolute;top:101px;left:0;font-size:10.5px;line-height:22.5px}
.review .more{position:absolute;top:233px;left:0;font-size:11px;font-weight:700;color:var(--accent);letter-spacing:.3px}

/* why */
.why{top:2371px;height:509px;background:var(--cream)}
.feature{position:absolute;top:2600px;width:204px;text-align:center;white-space:nowrap}
.feature svg{display:block;margin:0 auto}
.feature h4{font-family:'Libre Baskerville',serif;font-weight:400;font-size:15px;color:var(--ink);margin-top:22px}
.feature .rule{width:34px;height:2px;background:var(--accent);margin:8px auto 0}
.feature p{font-size:10.5px;line-height:22.5px;margin-top:14px}

/* contains */
.contains{top:2880px;height:637px;background:var(--white)}
.contents-head{left:161px;top:3203px;font-family:'Libre Baskerville',serif;font-size:15px;line-height:30px;color:var(--ink);white-space:nowrap}
.chapters{left:161px;font-family:'Libre Baskerville',serif;font-size:12.5px;text-transform:uppercase;color:var(--muted);display:flex;white-space:nowrap}
.chapters span{width:132px;border-right:1px solid #ddd;margin-right:14px}
.chapters span:last-child{border:none}
.chapters .on{color:var(--accent)}
.offer{left:302px;top:3391px;font-family:'Libre Baskerville',serif;font-style:italic;font-size:13px;color:var(--ink);white-space:nowrap}
.promo{left:611px;top:3185px;width:428px;height:255px;background:linear-gradient(135deg,#e4583b 0%,#e66a3f 60%,#f0b43c 100%)}
.dot{position:absolute;border-radius:50%;background:rgba(255,255,255,.55);width:11px;height:11px}
.dot.on{background:#fff;width:13px;height:13px}
</style>
</head>
<body>

<header class="hero">
  <nav class="nav">
    <a class="active" style="left:159px">Home</a>
    <a style="left:231px">About</a>
    <a style="left:309px">Storefront</a>
    <a style="left:736px">Coming Soon</a>
    <a style="left:869px">Featured</a>
    <a style="left:973px">Contact</a>
  </nav>
  <div class="brand">
    <div class="brand-name">MARGOT</div>
    <div class="brand-line"></div>
    <div class="brand-tag">Author &amp; Writer</div>
  </div>
  <div class="abs hero-title">
    <div class="l1">Meet Your Next</div>
    <div class="l2">Favorite Book</div>
  </div>
  <p class="abs hero-copy">Lorem ipsum dolor amet vegan butcher scenester, retro blue and<br>bottle yuccie synth kombucha celiac PBR&amp;B palo santo ugh lorei</p>
  <a class="btn" style="left:198px;top:385px;width:128px;height:43px">Take a look
    <svg width="11" height="9" viewBox="0 0 11 9"><path d="M0 4.5h9M6 1l3.5 3.5L6 8" fill="none" stroke="#fff" stroke-width="1.4"/></svg></a>
  <a class="btn ghost" style="left:349px;top:385px;width:129px;height:43px">Purchase
    <svg width="11" height="10" viewBox="0 0 11 10"><path d="M0 1h2l1.5 6h6L11 2.5H3" fill="none" stroke="#e4583b" stroke-width="1.3"/></svg></a>
  <div class="abs book-visual" role="img" aria-label="Hardcover book shown front and back, colourful children's chemistry cover"></div>
</header>

<section class="welcome">
  <div class="abs center title" style="top:110px">Welcome To Lorem Ipsum</div>
  <div class="abs center eyebrow" style="top:183px">Lorem ipsum dolor amet vegan butcher scenester, retro blue</div>
  <p class="abs lead" style="left:0;width:1200px;top:218px;text-align:center">Dreamcatcher cornhole subway tile tumeric tbh selvage PBR&amp;B. Fingerstache stumptown godard, man bu butcher echo park pitchfork<br>blue bottle VHS vaporware waistcoat four loko 90's bespoke. Kickstarter flannel vinyl blue bottle sriracha, cloud bread coloring book swag<br>meggings church-key helvetica polaroid subway tile pabst dreamcatcher</p>
</section>

<div class="abs eyebrow about-label">About Me</div>
<h2 class="abs about-head">Lorem Ipsatui<br>Dolor</h2>
<p class="abs about-copy">Lorem ipsum dolor sit amet, consectetu eradipisc-<br>ing elit. Aenean commodo ligula eget dolor. Simply.<br>Aenean massa. Cum sociis natoque penatibus et<br>magnis Lorem ipsum dolor sit amet, consectetuer<br>adipiscing elit. Cum sociisnatoque penatibus et ait</p>
<a class="btn" style="left:161px;top:1276px;width:130px;height:44px">More about me</a>
<div class="abs portrait" role="img" aria-label="Portrait photo of the author smiling, wearing a red top"></div>
<div class="abs quote-box">
  <div class="quote-mark abs" style="left:28px;top:26px">&ldquo;</div>
  <p class="quote-text">Lorem ipsum dolor<br>leanse food truck as<br>casmustache asymme<br>ricala mixtape of a<br>viral and of a known<br>at any typewriter</p>
  <div class="quote-mark abs" style="left:218px;top:200px">&rdquo;</div>
</div>

<section class="reviews">
  <div class="abs center eyebrow" style="top:74px">Book Reviews</div>
  <div class="abs center title" style="top:114px">Latest Reviews Of The Book</div>
  <a class="btn" style="left:535px;top:781px;width:130px;height:44px">View all</a>
</section>

<div class="cover" style="left:161px;top:1652px" role="img" aria-label="Book cover illustration"></div>
<div class="review" style="left:386px;top:1645px">
  <h3>What Simply Dummy Of<br>Text Is A Lorem Ipsum</h3>
  <div class="by">By: LOREM IPSUM</div>
  <p>Lorem ipsum dolor sit amet, consecte-<br>tu eradipiscing elit. Aenean commodo<br>ligula eget dolor. Simply. Aenean atn<br>massa. Cum sociis natoque penatibus<br>if any lorem ipsum is dolor</p>
  <div class="more">READ THE REVIEW &gt;&gt;</div>
</div>
<div class="cover" style="left:611px;top:1652px" role="img" aria-label="Book cover illustration"></div>
<div class="review" style="left:836px;top:1645px">
  <h3>What Simply Dummy Of<br>Text Is A Lorem Ipsum</h3>
  <div class="by">By: LOREM IPSUM</div>
  <p>Lorem ipsum dolor sit amet, consecte-<br>tu eradipiscing elit. Aenean commodo<br>ligula eget dolor. Simply. Aenean atn<br>massa. Cum sociis natoque penatibus<br>if any lorem ipsum is dolor</p>
  <div class="more">READ THE REVIEW &gt;&gt;</div>
</div>
<div class="cover" style="left:161px;top:1914px" role="img" aria-label="Book cover illustration"></div>
<div class="review" style="left:386px;top:1907px">
  <h3>What Simply Dummy Of<br>Text Is A Lorem Ipsum</h3>
  <div class="by">By: LOREM IPSUM</div>
  <p>Lorem ipsum dolor sit amet, consecte-<br>tu eradipiscing elit. Aenean commodo<br>ligula eget dolor. Simply. Aenean atn<br>massa. Cum sociis natoque penatibus<br>if any lorem ipsum is dolor</p>
  <div class="more">READ THE REVIEW &gt;&gt;</div>
</div>
<div class="cover" style="left:611px;top:1914px" role="img" aria-label="Book cover illustration"></div>
<div class="review" style="left:836px;top:1907px">
  <h3>What Simply Dummy Of<br>Text Is A Lorem Ipsum</h3>
  <div class="by">By: LOREM IPSUM</div>
  <p>Lorem ipsum dolor sit amet, consecte-<br>tu eradipiscing elit. Aenean commodo<br>ligula eget dolor. Simply. Aenean atn<br>massa. Cum sociis natoque penatibus<br>if any lorem ipsum is dolor</p>
  <div class="more">READ THE REVIEW &gt;&gt;</div>
</div>

<section class="why">
  <div class="abs center eyebrow" style="top:88px">Why Choosing It</div>
  <div class="abs center title" style="top:128px">Why Choosing This Book?</div>
</section>

<div class="feature" style="left:164px">
  <svg width="62" height="48" viewBox="0 0 62 48" fill="none" stroke="#e4583b" stroke-width="1.6"><path d="M31 8C24 3 12 3 4 5v36c8-2 20-2 27 3 7-5 19-5 27-3V5c-8-2-20-2-27 3zM31 8v36"/><path d="M10 13h15M10 19h15M10 25h15M37 13h15M37 19h15M37 25h15"/></svg>
  <h4>Lorem Ipsum Dolor</h4><div class="rule"></div>
  <p>Lorem ipsum dolor sit amet, &nbsp;tu eradip-<br>iscing elit. Aenean commodo ligula<br>eget dolor. Simply. Aenean atn massa.<br>Cum sociis natoque penatibus if any</p>
</div>
<div class="feature" style="left:389px">
  <svg width="54" height="50" viewBox="0 0 54 50" fill="none" stroke="#e4583b" stroke-width="1.6"><path d="M6 4h34v42H10a4 4 0 0 1-4-4z"/><path d="M12 14h20M12 21h20M12 28h14"/><path d="M48 6l-16 22-3 6 6-3 16-22z"/></svg>
  <h4>Lorem Ipsum Dolor</h4><div class="rule"></div>
  <p>Lorem ipsum dolor sit amet, &nbsp;tu eradip-<br>iscing elit. Aenean commodo ligula<br>eget dolor. Simply. Aenean atn massa.<br>Cum sociis natoque penatibus if any</p>
</div>
<div class="feature" style="left:614px">
  <svg width="52" height="50" viewBox="0 0 52 50" fill="none" stroke="#e4583b" stroke-width="1.6"><circle cx="26" cy="21" r="11"/><circle cx="26" cy="21" r="4"/><path d="M21 33h10v8H21zM23 45h6M26 2v4M9 21H4M48 21h-5M13 8l3 3M39 8l-3 3"/></svg>
  <h4>Lorem Ipsum Dolor</h4><div class="rule"></div>
  <p>Lorem ipsum dolor sit amet, &nbsp;tu eradip-<br>iscing elit. Aenean commodo ligula<br>eget dolor. Simply. Aenean atn massa.<br>Cum sociis natoque penatibus if any</p>
</div>
<div class="feature" style="left:839px">
  <svg width="46" height="52" viewBox="0 0 46 52" fill="none" stroke="#e4583b" stroke-width="1.6"><circle cx="23" cy="18" r="14"/><circle cx="23" cy="18" r="9"/><path d="M23 12l2 4 4 .5-3 3 .8 4-3.8-2-3.8 2 .8-4-3-3 4-.5z"/><path d="M14 29L7 46l7-3 4 6 5-13M32 29l7 17-7-3-4 6-5-13"/></svg>
  <h4>Lorem Ipsum Dolor</h4><div class="rule"></div>
  <p>Lorem ipsum dolor sit amet, &nbsp;tu eradip-<br>iscing elit. Aenean commodo ligula<br>eget dolor. Simply. Aenean atn massa.<br>Cum sociis natoque penatibus if any</p>
</div>

<section class="contains">
  <div class="abs center eyebrow" style="top:87px">A Closer Look</div>
  <div class="abs center title" style="top:126px">What This Book Contains</div>
  <p class="abs lead" style="left:0;width:1200px;top:179px;text-align:center">Dreamcatcher cornhole subway tile tumeric tbh selvage PBR&amp;B. Fingerstache stumptown godard, man bu butcher echo park pitchfork<br>blue bottle VHS vaporware waistcoat four loko 90's bespoke. Kickstarter flannel vinyl blue bottle sriracha, cloud bread coloring book swag<br>meggings church-key helvetica polaroid subway tile pabst dreamcatcher</p>
</section>

<div class="abs contents-head">What Simply Dummy Of &nbsp;Text Is A Lorem Ipsum And<br>Lorem Dolor Amet</div>
<div class="abs chapters" style="top:3280px"><span class="on">Chapter One</span><span style="width:136px">Chapter Two</span><span>Chapter Three</span></div>
<div class="abs chapters" style="top:3317px"><span>Chapter Four</span><span style="width:136px">Chapter Five</span><span>Chapter Six</span></div>
<a class="btn" style="left:161px;top:3377px;width:130px;height:44px">Purchase
  <svg width="11" height="10" viewBox="0 0 11 10"><path d="M0 1h2l1.5 6h6L11 2.5H3" fill="none" stroke="#fff" stroke-width="1.3"/></svg></a>
<div class="abs offer">Get the book with 30% off !</div>
<div class="abs promo" role="img" aria-label="Colourful illustrated book page with a microscope and a child celebrating learning chemistry">
  <span class="dot" style="left:391px;top:97px"></span>
  <span class="dot on" style="left:390px;top:117px"></span>
  <span class="dot" style="left:391px;top:139px"></span>
</div>

</body>
</html>
```